Heath Weight Loss Retreat Website

The brief:
PineLoop is a provider of health & weight loss retreats and wish to redesign their main website. The website needs to provide detailed information about the company’s services whilst gathering the maximum number of leads possible. The website does not aim to get clients to ‘book now’ but to request further information, or ask a question generating a lead/opportunity for the business.

Primary objectives of website
• Gather leads for products (not necessarily to book at that point, but to ‘request more info’)
• Provide detailed information about the health and fitness programs on offer

Demographic Considerations
• Target age group: 30-50
• Predominant client base are female but website should be gender neutral due to some men attending

Design considerations
• Essentially selling ‘travel experiences’ and ‘life transformations’ so needs to be lots of images to display (similar to a hotel website for example)
• Images need to display real people – i.e. larger people, rather than super thin
• Not too much use of flash
• SEO friendly (we have good rankings at present)
• Will be implemented into Joomla, so please consider this on the design
• Colours should be ‘warm’ and ‘friendly’ and gender neutral

Project Requirements & Expectations
Please supply your design ideas with:
• At least 1 (preferably more) homepage examples
• At least 1 (preferably more) internal page examples
Once a preferred design has been selected the following will be produced, tweaked and approved:
• Homepage + 1 internal landing page + 1 internal main page + 1 contact page + 1 info request page

Attachments
We have attached both a homepage and internal page example which demonstates the type of content needed and the calls to action. This is for demonstration purposes only so please ignore colours, fonts, etc and provide your best designs based on a general layout as per attached.

Images:
A selection of example images has been attached. For the homepage images of the retreats themselves should be used alongside images of ‘larger people’.

Further information:
Please contact Simon Thackery at simon.thackery@coralbeaconfiles.com.au

Target Market(s)

Overweight females aged 30-50 are the main target market. However must be gender neutral due to some men using product.

Industry/Entity Type

Weight

Requirements
Should not have
• Not too much flash

```html
<!DOCTYPE html>
<html lang="en">
<head>
<meta charset="utf-8">
<title>PineLoop Weight Loss Retreat</title>
<link href="https://fonts.googleapis.com/css2?family=Arimo:ital,wght@0,400;0,700;1,400&display=swap" rel="stylesheet">
<style>
:root{
  --blue-dark:#0a4ea8;
  --blue:#1d6fd1;
  --blue-light:#3b8be0;
  --gold:#f5c400;
  --yellow-text:#ffe14a;
  --red:#e00000;
  --red-dark:#b80000;
  --green:#2a8a1e;
  --green-dark:#17630f;
  --sand:#fcc862;
  --ink:#111;
  --footer:#111;
  --footer-base:#000;
  --white:#fff;
}
*{margin:0;padding:0;box-sizing:border-box}
html,body{width:812px;height:1200px;overflow:hidden;background:var(--white)}
body{position:relative;font-family:"Arimo",Arial,sans-serif;color:var(--ink)}
.abs{position:absolute}

/* header */
.site-header{left:0;top:0;width:812px;height:157px;background:linear-gradient(180deg,var(--blue-dark) 0%,var(--blue) 60%,var(--blue-light) 100%);border-top:2px solid #7fc12a}
.brand{left:83px;top:50px;width:112px;text-align:center;color:var(--white)}
.brand-name{font-size:24px;font-weight:700;letter-spacing:-0.5px;line-height:1}
.brand-tag{font-size:7px;font-weight:700;text-align:right;margin-top:2px}
.nav-col{top:9px}
.nav-col h3{font-size:11px;font-weight:700;color:var(--yellow-text);margin-bottom:4px}
.nav-col li{list-style:none;font-size:7.3px;color:var(--white);line-height:12.8px}
.nav-col li::before{content:"» "}
.magazine{left:669px;top:17px;width:67px;height:76px}
.magazine-cover{width:100%;height:100%;background:linear-gradient(180deg,#c9d9ea,#8da6c2);border:1px solid #ddd}
.magazine-tag{position:absolute;left:0;bottom:0;width:100%;height:30px;background:var(--red);color:var(--white);text-align:center;font-weight:700;font-size:17px;line-height:24px}
.magazine-tag small{display:block;font-size:5px;line-height:5px}

/* hero */
.hero{left:81px;top:99px;width:655px;height:258px;background:var(--white);border:1px solid #ccc;padding:5px}
.hero-photo{position:relative;width:100%;height:100%;background:linear-gradient(180deg,#9ea5a4 0%,#c8cbc4 40%,#5b7a3a 62%,#4f6e2e 100%);overflow:hidden}
.hero-figure{position:absolute;right:0;top:0;width:320px;height:100%;background:linear-gradient(90deg,rgba(220,200,185,0) 0%,rgba(225,205,190,.85) 25%,rgba(235,225,215,.95) 60%,rgba(200,185,170,.8) 100%)}
.hero-copy{position:absolute;left:48px;top:78px;color:var(--white);text-shadow:0 1px 3px rgba(0,0,0,.6)}
.hero-copy h1{font-size:19px;font-weight:700;line-height:25px}
.hero-copy p{font-size:12.5px;line-height:17px;margin-top:6px}
.hero-arrow{position:absolute;top:112px}

/* intro */
.intro{left:82px;top:366px;width:390px}
.intro-lead{font-size:10.5px}
.intro-quote{font-size:17.5px;margin-top:3px}
.btn{position:absolute;top:406px;height:27px;border-radius:5px;color:var(--white);font-size:12px;line-height:27px;text-align:center}
.btn-info{left:87px;width:186px;background:linear-gradient(180deg,#e21a1a,var(--red-dark))}
.btn-more{left:280px;width:112px;background:linear-gradient(180deg,#4e8fe0,#1b58b0)}
.body-copy{left:89px;top:444px;width:378px;font-size:6.6px;line-height:11.7px}
.body-copy p{margin-bottom:11.6px;text-align:justify}

/* program list */
.programs{left:478px;top:357px;width:129px;height:309px;background:linear-gradient(90deg,#ddd,#f4f4f4);border:1px solid #ccc}
.panel-title{font-size:12px;font-style:italic;color:#444;padding:8px 0 0 11px}
.panel-sub{font-size:6.5px;font-weight:700;color:#333;padding-left:11px}
.program{position:absolute;left:0;width:127px}
.program h4{background:var(--red);color:var(--white);font-size:7px;font-weight:700;padding:1px 10px;height:11px;line-height:9px}
.program p{font-size:6.8px;color:#333;padding-left:10px;line-height:10.5px}
.program p.strong{font-weight:700}

/* right column */
.side{left:614px;top:357px;width:122px}
.side .panel-title{padding:8px 0 0 1px}
.side .panel-sub{padding-left:1px;font-weight:400}
.location{position:absolute;left:0;width:122px;color:var(--white);padding:0 3px}
.location h4{font-size:9px;font-weight:700}
.location p{font-size:5px;line-height:6px}
.loc-blue{top:37px;height:66px;background:linear-gradient(180deg,#8fb6d8 0%,#5c7fa3 50%,#2e4a6a 100%);border:1px solid #7aa0c8;padding-top:31px}
.loc-sunshine{top:110px;height:38px;background:linear-gradient(90deg,#6b3a10,#a0621f);padding-top:5px}
.goal{position:absolute;top:154px;left:0;width:122px;height:57px;background:linear-gradient(180deg,#333,#222);color:var(--white);padding:5px 6px}
.goal h4{font-size:8.5px;font-weight:700;margin-bottom:1px}
.goal p{font-size:5px;line-height:6px;font-weight:700}
.goal-field{display:flex;gap:3px;margin-top:4px}
.goal-input{width:90px;height:12px;background:var(--white);color:#888;font-size:5.5px;line-height:12px;padding-left:3px}
.goal-go{width:14px;height:12px;background:var(--red);border:1px solid var(--white);font-size:6px;font-weight:700;text-align:center;line-height:10px}
.quote-box{position:absolute;top:218px;left:0;width:122px;height:91px;background:linear-gradient(180deg,#eee,#d6d6d6);padding:6px 3px 6px 8px}
.quote-mark{font-size:26px;font-weight:700;line-height:18px;font-family:Georgia,serif}
.quote-box p{font-size:11.2px;line-height:15px;color:#222;letter-spacing:-0.2px;white-space:nowrap}
.quote-close{position:absolute;right:8px;top:56px;font-size:22px;font-weight:700;font-family:Georgia,serif}
.quote-nav{position:absolute;right:6px;bottom:5px;display:flex;gap:2px}
.quote-nav span{width:9px;height:9px;background:#666;border-radius:2px}

/* real results */
.real{left:478px;top:676px;width:258px;height:156px;border-radius:6px;background:linear-gradient(180deg,var(--green-dark),var(--green));color:var(--white);padding:10px 11px}
.real h3{font-size:14px;font-weight:400;margin-bottom:7px}
.real li{list-style:none;font-size:11px;line-height:18px}
.real li::before{content:"» "}
.real-link{position:absolute;left:7px;top:103px;width:150px;height:18px;background:var(--white);border-radius:9px;color:var(--green);font-size:10.5px;line-height:18px;padding-left:8px}
.real-photo{position:absolute;width:62px;height:62px;border-radius:50%;border:2px solid var(--white)}
.rp-1{left:192px;top:59px;background:linear-gradient(180deg,#c9d9ea,#6b88b0)}
.rp-2{left:146px;top:87px;background:linear-gradient(180deg,#f2b8c8,#d68aa0)}

/* results list */
.results{left:478px;top:841px;width:258px;height:173px;border-radius:6px;background:var(--sand);overflow:hidden}
.results-head{height:30px;background:linear-gradient(180deg,#2a62c0,#1a4ea3);clip-path:polygon(0 0,100% 0,100% 70%,0 100%);color:var(--white);font-size:13.5px;padding:5px 11px}
.results-cols{display:flex;padding:9px 4px 0 7px;gap:4px}
.results-cols ul{list-style:none;width:127px}
.results-cols li{font-size:7.5px;line-height:12.8px;padding-left:11px;position:relative}
.results-cols li::before{content:"✓";position:absolute;left:0;font-weight:700}

/* footer */
.footer{left:0;top:1022px;width:812px;height:155px;background:var(--footer);border-top:4px solid var(--gold)}
.foot-col{position:absolute;top:20px;height:130px}
.foot-col h3{font-size:10.5px;font-weight:400;color:var(--gold);margin-bottom:13px}
.foot-col li{list-style:none;font-size:7.6px;color:#eee;line-height:14px}
.foot-divider{position:absolute;top:14px;width:1px;height:133px;background:#333}
.base{left:0;top:1177px;width:812px;height:23px;background:var(--footer-base);color:#999;font-size:6.5px;line-height:23px}
.base-links{position:absolute;left:92px}
.base-copy{position:absolute;right:76px}
</style>
</head>
<body>

<header class="site-header abs">
  <div class="brand abs">
    <div class="brand-name">PineLoop</div>
    <div class="brand-tag">WEIGHT LOSS RETREAT</div>
  </div>
  <nav class="nav-col abs" style="left:246px">
    <h3>The Best Programs</h3>
    <ul><li>Weight Loss Retreat</li><li>Residential Boot Camp</li><li>Fitness Days</li><li>At home program</li><li>Local group exercise</li></ul>
  </nav>
  <nav class="nav-col abs" style="left:376px">
    <h3>The Best Locations</h3>
    <ul><li>Blue Mountains, NSW</li><li>Sunshine Coast, QLD</li><li>Local Programs</li></ul>
  </nav>
  <nav class="nav-col abs" style="left:513px">
    <h3>Act now and get results</h3>
    <ul><li>Why choose PineLoop</li><li>Expert Team</li><li>What clients say...</li><li>Contact us</li><li>FREE Brochure</li></ul>
  </nav>
  <div class="magazine abs">
    <div class="magazine-cover" role="img" aria-label="PineLoop magazine cover"></div>
    <div class="magazine-tag">FREE<small>PineLoop Magazine</small></div>
  </div>
</header>

<section class="hero abs">
  <div class="hero-photo" role="img" aria-label="Larger man in a white cap and t-shirt sitting on a grassy field">
    <div class="hero-figure"></div>
    <svg class="hero-arrow" style="left:6px" width="30" height="34" viewBox="0 0 30 34"><polyline points="24,3 8,17 24,31" fill="none" stroke="#fff" stroke-width="6"/></svg>
    <svg class="hero-arrow" style="right:6px" width="30" height="34" viewBox="0 0 30 34"><polyline points="6,3 22,17 6,31" fill="none" stroke="#fff" stroke-width="6"/></svg>
    <div class="hero-copy">
      <h1>Amazing weight loss &amp; fitness results<br>Lasting results &amp; 1st class facilities</h1>
      <p>PineLoop has helped hundreds of people transform their<br>lives, lose weight, get fit and achieve lasting success.<br>Let us help you too...</p>
    </div>
  </div>
</section>

<section class="intro abs">
  <p class="intro-lead">The PineLoop program works – as one client put it....</p>
  <p class="intro-quote">“The best weight loss experience of my life”</p>
</section>
<a class="btn btn-info">Request a FREE Information Pack</a>
<a class="btn btn-more">More testimonials</a>

<article class="body-copy abs">
  <p>Hundreds of people have already transformed their lives with PineLoop's proven programs. With PineLoop you will lose weight, lose centimetres, get fit and experience lasting health and fitness results.</p>
  <p>Our Weight Loss Retreat program is suitable for people of all ages, shapes, sizes and fitness levels – whether you have 5kgs to lose, or 100kgs to lose this program is right for you. It is amazingly fun and extremely effective with amazing weight loss results, fantastic fitness results, and significant health improvements. Whether you want a kick start or are embarking on a long term weight loss program our Weight Loss Retreat program will be one of the best experiences of your life – that's our promise to you.</p>
  <p>program is right for you. It is amazingly fun and extremely effective with amazing weight loss results, fantastic fitness results, and significant health improvements. Whether you want a kick start or are embarking on a long term weight loss program our Weight Loss Retreat program will be one of the best experiences of your life – that's our promise to you.</p>
  <p>program is right for you. It is amazingly fun and extremely effective with amazing weight loss results, fantastic fitness results, and significant health improvements. Whether you want a kick start or are embarking on a long term weight loss program our Weight Loss Retreat program will be one of the best experiences of your life – that's our promise to you.</p>
  <p>program is right for you. It is amazingly fun and extremely effective with amazing weight loss results, fantastic fitness results, and significant health improvements. Whether you want a kick start or are embarking on a long term weight loss program our Weight Loss Retreat program will be one of the best experiences of your life – that's our promise to you.</p>
  <p>program is right for you. It is amazingly fun and extremely effective with amazing weight loss results, fantastic fitness results, and significant health improvements. Whether you want a kick start or are embarking on a long term weight loss program our Weight Loss Retreat program will be one of the best experiences of your life – that's our promise to you.</p>
  <p>program is right for you. It is amazingly fun and extremely effective with amazing weight loss results, fantastic fitness results, and significant health improvements. Whether you want a kick start or are embarking on a long term weight loss program our Weight Loss Retreat program will be one of the best experiences of your life – that's our promise to you.</p>
  <p>program is right for you. It is amazingly fun and extremely effective with amazing weight loss results, fantastic fitness results, and significant health improvements. Whether you want a kick start or are embarking on a long term weight loss program our Weight Loss Retreat program will be one of the best experiences of your life – that's our promise to you.</p>
  <p>program is right for you. It is amazingly fun and extremely effective with amazing weight loss results, fantastic fitness results, and significant health improvements. Whether you want a kick start or are embarking on a long term weight loss program our Weight Loss Retreat program will be one of the best experiences of your life – that's our promise to you.</p>
  <p>program is right for you. It is amazingly fun and extremely effective with amazing weight loss results, fantastic fitness results, and significant health improvements. Whether you want a kick start or are embarking on a long term weight loss program our Weight Loss Retreat program will be one of the best experiences of your life – that's our promise to you.</p>
  <p>program is right for you. It is amazingly fun and extremely effective with amazing weight loss results, fantastic fitness results, and significant health improvements. Whether you want a kick start or are embarking on a long term weight loss program our Weight Loss Retreat program will be one of the best experiences of your life – that's our promise to you.</p>
  <p>program is right for you. It is amazingly fun and extremely effective with amazing weight loss results, fantastic fitness results, and significant health improvements. Whether you want a kick start or are embarking on a long term weight loss program our Weight Loss Retreat program will be one of the best experiences of your life – that's our promise to you.</p>
</article>

<aside class="programs abs">
  <p class="panel-title">The best programs...</p>
  <p class="panel-sub">BOOK NOW &gt;&gt;</p>
  <div class="program" style="top:36px"><h4>Weight Loss Retreat</h4><p>Lasting weight loss results</p><p>Program details | Typical Day</p><p>Dates &amp; Rates | FREE Brochure</p></div>
  <div class="program" style="top:88px"><h4>Residential Boot Camp</h4><p class="strong">Kick start your health &amp; fitness</p><p>Program details | Typical Day</p><p>Dates &amp; Rates | FREE Brochure</p></div>
  <div class="program" style="top:140px"><h4>At Home Program</h4><p>Do it yourself with our home pack</p><p>Program details | FREE Brochure</p></div>
  <div class="program" style="top:182px"><h4>Fitness Days</h4><p>Have fun and keep on track</p><p>Program overview | Typical Day</p><p>Dates &amp; Rates | FREE Brochure</p></div>
  <div class="program" style="top:234px"><h4>Local Group Exercise</h4><p class="strong">Get fit &amp; lose weight locally</p><p>Overview | Times &amp; Locations</p></div>
  <div class="program" style="top:275px"><h4>Personal Training for you</h4><p>Find an approved PineLoop Trainer</p></div>
</aside>

<aside class="side abs">
  <p class="panel-title">The best programs...</p>
  <p class="panel-sub">&amp; 1st class facilities</p>
  <div class="location loc-blue" role="img" aria-label="Guest standing above a mountain valley">
    <h4>Blue Mountains ****</h4>
    <p>4 star accommodation, stunning mountain scenery &amp; 1st class facilities</p>
    <p>Find out more | FREE Brochure | Book</p>
  </div>
  <div class="location loc-sunshine" role="img" aria-label="Coastal retreat accommodation">
    <h4>Sunshine Coast ****</h4>
    <p>4.5 star accommodation</p>
    <p>Find out more | FREE Brochure | Book</p>
  </div>
  <div class="goal">
    <h4>Your goal selector</h4>
    <p>tell us your goal and we'll tell you how PineLoop can help:</p>
    <div class="goal-field"><div class="goal-input">Select your primary goal</div><div class="goal-go">Go</div></div>
  </div>
  <div class="quote-box">
    <div class="quote-mark">“</div>
    <p>The best weight loss<br>experience of my life.</p>
    <div class="quote-close">”</div>
    <div class="quote-nav"><span></span><span></span></div>
  </div>
</aside>

<section class="real abs">
  <h3>Real People – Real Results</h3>
  <ul><li>100’s of people helped by PineLoop</li><li>People of all ages, shapes, and sizes</li><li>Normal people just like you</li></ul>
  <div class="real-link">Testimonials and reviews »</div>
  <div class="real-photo rp-1" role="img" aria-label="Client portrait"></div>
  <div class="real-photo rp-2" role="img" aria-label="Client measuring her waist"></div>
</section>

<section class="results abs">
  <div class="results-head">Results our clients have achieved</div>
  <div class="results-cols">
    <ul><li>Weight loss</li><li>Fat loss</li><li>Lose centimetres of your waist, hips, thighs and from all over your body</li><li>Increased flexibility</li><li>Improved mobility and agility</li><li>Transform your skin condition</li><li>Feel happier</li><li>Better sleep patterns</li></ul>
    <ul><li>Eliminate high blood pressure</li><li>Eliminate Type 2 Diabetes</li><li>Reduce cholesterol issues</li><li>Improve previous injuries</li><li>Reduce head aches</li><li>Reduce stress</li><li>No more anxiety</li><li>Significant improvements for those suffering depresion</li></ul>
  </div>
</section>

<footer class="footer abs">
  <div class="foot-col" style="left:93px"><h3>The Best Programs</h3><ul><li>Weight Loss Retreat</li><li>Residential Boot Camp</li><li>Fitness Days</li><li>At home program</li><li>Local group exercise</li></ul></div>
  <div class="foot-divider" style="left:208px"></div>
  <div class="foot-col" style="left:223px"><h3>The Best Locations</h3><ul><li>Blue Mountains, NSW</li><li>Sunshine Coast, QLD</li><li>Local Programs</li></ul></div>
  <div class="foot-divider" style="left:340px"></div>
  <div class="foot-col" style="left:360px"><h3>About Us</h3><ul><li>Why choose PineLoop</li><li>Expert Team</li><li>What clients say....</li><li>Contact us</li><li>Book now</li></ul></div>
  <div class="foot-divider" style="left:470px"></div>
  <div class="foot-col" style="left:490px"><h3>Results for...</h3><ul><li>Weight Loss</li><li>Fitness goals</li><li>Diabetes reduction</li><li>Blood pressure reduction</li><li>Depression improvement</li><li>More Health Benefits</li></ul></div>
  <div class="foot-divider" style="left:604px"></div>
  <div class="foot-col" style="left:621px"><h3>FREE Information</h3><ul><li>Request a brochure</li><li>FREE PineLoop Magazine</li></ul></div>
</footer>
<div class="base abs">
  <span class="base-links">Contact Us | Book Now | Privacy</span>
  <span class="base-copy">(C) PineLoop Wellbeing PTY Ltd | ABN 1234567987</span>
</div>

</body>
</html>
```